Graduation Day Sale Banner Ad for Website

We need a banner for our upscale jewelry website. Banner must have a classy high end look. The size of the banner must be 1187 × 400. I have attached pieces we would like used (some or all). The banner is for a Graduation Day sale that we are running. The banner should say "Graduation Day Gifts on Sale"

Target Market(s)

Wealthy individuals looking to buy graduation gifts for their children

Industry/Entity Type

Jewelry

Requirements
Must have
• Must match the look and feel of the website (www.fenlustre.com)

```html
<!DOCTYPE html>
<html lang="en">
<head>
<meta charset="utf-8">
<title>Fenlustre – Graduation Day Gifts on Sale</title>
<link href="https://fonts.googleapis.com/css2?family=Open+Sans:wght@400;600&family=Great+Vibes&family=Montserrat:wght@800&display=swap" rel="stylesheet">
<style>
  :root {
    --page: #ffffff;
    --ink: #3a3a3a;
    --muted: #6b6b6b;
    --nav: #9c7f6b;
    --banner-bg: #f2e6dd;
    --banner-bg-2: #e9d8cc;
    --frame: #8f7565;
    --script: #4e2d1b;
    --gifts: #6a5247;
    --parcel: #b9977f;
    --sale-red: #f0232a;
    --band: #d6c4b6;
    --band-btn: #7c6050;
    --corner: #e8c9a0;
  }
  * { box-sizing: border-box; margin: 0; padding: 0; }
  html, body { width: 1200px; height: 580px; overflow: hidden; background: var(--page); }
  body { position: relative; font-family: "Open Sans", Arial, sans-serif; color: var(--ink); }

  .util { position: absolute; top: 8px; font-size: 14px; letter-spacing: 1px; display: flex; align-items: center; gap: 8px; color: var(--ink); }
  .util svg { stroke: var(--nav); fill: none; stroke-width: 1.4; }
  .util-phone { left: 582px; }
  .util-sell { left: 754px; }
  .util-sign { left: 908px; font-size: 12px; }

  .brand { position: absolute; left: 155px; top: 48px; width: 290px; }
  .brand-name { font-size: 62px; font-weight: 400; color: #111; line-height: 1; letter-spacing: 1px; }
  .brand-tag { font-size: 15px; color: #111; margin-top: 14px; letter-spacing: 0.3px; }

  .search { position: absolute; left: 540px; top: 57px; width: 259px; height: 26px; border-bottom: 1px solid #999; display: flex; align-items: center; }
  .search-label { font-size: 11px; color: #777; margin-left: 38px; }
  .search svg.lens { position: absolute; left: 9px; top: 5px; stroke: #aaa; fill: none; stroke-width: 1.3; }
  .search-btn { position: absolute; right: 0; top: 0; width: 30px; height: 25px; background: var(--nav); display: flex; align-items: center; justify-content: center; }

  .quick { position: absolute; top: 44px; display: flex; flex-direction: column; align-items: center; gap: 6px; font-size: 11px; letter-spacing: 1px; }
  .quick svg { stroke: var(--muted); fill: none; stroke-width: 1.4; }
  .quick-news { left: 831px; }
  .quick-wish { left: 925px; }
  .quick-cart { left: 1000px; }

  .nav { position: absolute; left: 467px; top: 107px; height: 38px; display: flex; gap: 1px; }
  .nav a { background: var(--nav); color: #fff; text-decoration: none; font-size: 15.5px; letter-spacing: 1px; display: flex; align-items: center; padding: 0 19px; }

  .corner { position: absolute; right: 0; top: 0; }

  .banner { position: absolute; left: 151px; top: 186px; width: 898px; height: 301px; overflow: hidden;
    background: linear-gradient(115deg, var(--banner-bg) 0%, #f7eee8 45%, var(--banner-bg-2) 100%); }
  .banner-frame { position: absolute; inset: 0; }
  .headline-script { position: absolute; left: 27px; top: 78px; font-family: "Great Vibes", cursive; font-size: 82px; color: var(--script); line-height: 1; white-space: nowrap; }
  .headline-main { position: absolute; left: 68px; top: 162px; font-family: "Montserrat", Arial, sans-serif; font-weight: 800; font-size: 41px; color: var(--gifts); letter-spacing: 1px; }
  .ring-photo { position: absolute; left: 527px; top: 62px; width: 140px; height: 116px; border-radius: 50%;
    background: radial-gradient(ellipse at 50% 50%, #f3ead9 0%, #e6c47c 40%, #cf9e4a 65%, rgba(240,225,210,0) 100%); }
  .gift-art { position: absolute; left: 419px; top: 184px; width: 339px; height: 117px;
    background: linear-gradient(180deg, rgba(185,151,127,0) 0%, rgba(185,151,127,0.75) 35%, var(--parcel) 100%); }
  .sale-art { position: absolute; left: 708px; top: 50px; width: 160px; height: 136px;
    background: radial-gradient(ellipse at 55% 55%, rgba(240,35,42,0.95) 0%, rgba(240,35,42,0.75) 45%, rgba(240,35,42,0) 72%); }

  .arrivals { position: absolute; left: 153px; top: 519px; width: 890px; height: 46px; background: var(--band); }
  .arrivals-title { position: absolute; left: 0; right: 0; top: 8px; text-align: center; color: #fff; font-size: 25px; letter-spacing: 1px; }
  .arrivals-btn { position: absolute; right: 9px; top: 9px; height: 31px; padding: 0 10px; background: var(--band-btn); color: #fff; font-size: 13px; letter-spacing: 0.5px; display: flex; align-items: center; }
</style>
</head>
<body>

  <div class="util util-phone">
    <svg width="16" height="16" viewBox="0 0 16 16"><path d="M3 1.5l2.5 0 1.2 3-1.6 1.2c.8 1.8 2.3 3.3 4.1 4.1l1.2-1.6 3 1.2v2.5c0 .8-.7 1.4-1.5 1.3C6.5 12.6 3.4 9.5 2.7 3 2.6 2.2 3.2 1.5 3 1.5z"/></svg>
    <span>800 - 555 - 0142</span>
  </div>
  <div class="util util-sell">
    <svg width="16" height="14" viewBox="0 0 16 14"><path d="M1 5l3-4h8l3 4-7 8z M1 5h14 M5.5 5L8 13l2.5-8"/></svg>
    <span>SELL JEWELRY</span>
  </div>
  <div class="util util-sign">
    <svg width="16" height="16" viewBox="0 0 16 16"><circle cx="8" cy="5" r="3.5"/><path d="M1.5 15c0-3.5 3-5.5 6.5-5.5s6.5 2 6.5 5.5z"/></svg>
    <span>SIGN IN / REGISTER</span>
  </div>

  <div class="brand">
    <div class="brand-name">Fenlustre</div>
    <div class="brand-tag">FINE ESTATE AND DESIGNER JEWELRY</div>
  </div>

  <div class="search">
    <svg class="lens" width="14" height="14" viewBox="0 0 14 14"><circle cx="6" cy="6" r="4.5"/><path d="M9.5 9.5l3.5 3.5"/></svg>
    <span class="search-label">Search</span>
    <div class="search-btn">
      <svg width="13" height="10" viewBox="0 0 13 10"><path d="M1 5l3.5 3.5L12 1" stroke="#fff" stroke-width="2" fill="none"/></svg>
    </div>
  </div>

  <div class="quick quick-news">
    <svg width="22" height="16" viewBox="0 0 22 16"><rect x="1" y="1" width="20" height="14"/><path d="M1 1l10 8 10-8"/></svg>
    <span>NEWSLETTER</span>
  </div>
  <div class="quick quick-wish">
    <svg width="22" height="20" viewBox="0 0 22 20"><path d="M11 18.5S1.5 12.5 1.5 6.5C1.5 3.5 3.8 1.5 6.3 1.5c2 0 3.6 1.2 4.7 3 1.1-1.8 2.7-3 4.7-3 2.5 0 4.8 2 4.8 5 0 6-9.5 12-9.5 12z"/></svg>
    <span>WISHLIST</span>
  </div>
  <div class="quick quick-cart">
    <svg width="22" height="20" viewBox="0 0 22 20"><path d="M1 1.5h3.5l2.5 11h11l2-8H6"/><circle cx="8.5" cy="17" r="1.5"/><circle cx="16.5" cy="17" r="1.5"/></svg>
    <span>CART (0)</span>
  </div>

  <nav class="nav">
    <a>FINE JEWELRY</a>
    <a>TIMEPIECES</a>
    <a>ACCESSORIES</a>
    <a>DESIGNERS</a>
    <a>SALE</a>
  </nav>

  <svg class="corner" width="94" height="92" viewBox="0 0 94 92">
    <polygon points="0,0 94,0 94,92" fill="var(--corner)"/>
    <text x="0" y="0" transform="translate(48,14) rotate(45)" font-family="Open Sans, sans-serif" font-size="14" fill="#333">Sign up!</text>
    <polygon points="80,14 86,14 86,20" fill="#333"/>
  </svg>

  <section class="banner">
    <svg class="banner-frame" width="898" height="301" viewBox="0 0 898 301">
      <path d="M386 283H15V18H881V283H784" fill="none" stroke="var(--frame)" stroke-width="2"/>
      <path d="M480 250A138 138 0 1 1 740 250" fill="none" stroke="var(--frame)" stroke-width="2"/>
    </svg>
    <div class="headline-script">Graduation Day</div>
    <div class="headline-main">GIFTS ON SALE</div>
    <div class="ring-photo" role="img" aria-label="Gold bypass ring set with two pearls and diamond accents"></div>
    <div class="sale-art" role="img" aria-label="Red hanging price tag reading sale"></div>
    <div class="gift-art" role="img" aria-label="Row of wrapped gift boxes and shopping bags in soft taupe"></div>
  </section>

  <section class="arrivals">
    <div class="arrivals-title">NEW ARRIVALS</div>
    <div class="arrivals-btn">VIEW ALL</div>
  </section>

</body>
</html>
```